Timber Ridge Land Services Business Cards

Need to create a business card with the company logo "Timber Ridge Land Services". The business will provide forestry mulching for land clearing and vegetation control, brush and small tree removal, wildlife habitat improvement and trail and property access creation.

```html
<!DOCTYPE html>
<html lang="en">
<head>
<meta charset="utf-8">
<title>Timber Ridge Land Services – Business Cards</title>
<link rel="stylesheet" href="https://fonts.googleapis.com/css2?family=Open+Sans:wght@400;600;700;800&display=swap">
<style>
  :root {
    --bg: #e4e5e7;
    --card: #ffffff;
    --forest: #0b5a3a;
    --leaf: #5cc062;
    --text: #555a5e;
    --rule: #d5d8d6;
  }
  * { margin: 0; padding: 0; box-sizing: border-box; }
  html, body { width: 1200px; height: 800px; overflow: hidden; }
  body {
    background: var(--bg);
    font-family: "Open Sans", Arial, sans-serif;
    position: relative;
  }
  .card {
    position: absolute;
    top: 246px;
    width: 540px;
    height: 309px;
    background: var(--card);
    box-shadow: 0 6px 18px rgba(0,0,0,0.12);
    overflow: hidden;
  }
  .card--services { left: 40px; }
  .card--contact { left: 620px; }
  .card__band {
    position: absolute;
    inset: 0;
    background: linear-gradient(100deg, var(--forest) 0%, var(--leaf) 70%);
    clip-path: polygon(0 150px, 260px 215px, 540px 258px, 540px 309px, 0 309px);
  }
  .brand {
    position: absolute;
    left: 44px;
    top: 58px;
    display: flex;
    align-items: center;
    gap: 10px;
    color: var(--forest);
    font-weight: 800;
    font-size: 19px;
    line-height: 1.1;
    letter-spacing: 0.5px;
    text-transform: uppercase;
  }
  .brand__mark { width: 14px; height: 14px; background: var(--leaf); border-radius: 50%; flex: none; }
  .divider {
    position: absolute;
    left: 300px;
    top: 108px;
    width: 1px;
    height: 100px;
    background: var(--rule);
  }
  .info { position: absolute; left: 318px; top: 92px; }
  .info__heading {
    color: var(--forest);
    font-weight: 700;
    font-size: 14px;
    text-transform: uppercase;
    margin-bottom: 6px;
  }
  .services { list-style: none; color: var(--text); font-size: 11.5px; line-height: 1.45; }
  .person__name { color: var(--forest); font-weight: 700; font-size: 14px; text-transform: uppercase; }
  .person__role { color: var(--leaf); font-weight: 600; font-size: 12px; margin-bottom: 12px; }
  .contacts { list-style: none; color: var(--text); font-size: 11.5px; line-height: 1.6; }
  .contacts li { display: flex; align-items: center; gap: 7px; }
  .contacts svg { width: 11px; height: 11px; fill: var(--forest); flex: none; }
</style>
</head>
<body>

<section class="card card--services">
  <div class="card__band" role="img" aria-label="Green decorative band across the lower card"></div>
  <div class="brand"><span class="brand__mark"></span><span>Timber Ridge<br>Land Services</span></div>
  <div class="divider"></div>
  <div class="info">
    <h2 class="info__heading">Our Services</h2>
    <ul class="services">
      <li>Forestry Mulching For Land Clearing</li>
      <li>And Vegetation Control</li>
      <li>Brush And Small Tree Removal</li>
      <li>Wildlife Habitat Improvement And Trail</li>
      <li>Property Access Creation</li>
    </ul>
  </div>
</section>

<section class="card card--contact">
  <div class="card__band" role="img" aria-label="Green decorative band across the lower card"></div>
  <div class="brand"><span class="brand__mark"></span><span>Timber Ridge<br>Land Services</span></div>
  <div class="divider"></div>
  <div class="info">
    <h2 class="person__name">John Smith</h2>
    <p class="person__role">Founder</p>
    <ul class="contacts">
      <li><svg viewBox="0 0 24 24"><path d="M6.6 10.8a15 15 0 0 0 6.6 6.6l2.2-2.2a1 1 0 0 1 1-.25 11.4 11.4 0 0 0 3.6.57 1 1 0 0 1 1 1V20a1 1 0 0 1-1 1A17 17 0 0 1 3 4a1 1 0 0 1 1-1h3.5a1 1 0 0 1 1 1c0 1.25.2 2.45.57 3.57a1 1 0 0 1-.25 1z"/></svg>555-014-2877</li>
      <li><svg viewBox="0 0 24 24"><path d="M2 5h20v14H2z M2 5l10 8 10-8" stroke="#fff" stroke-width="1.5"/></svg>info@timberridgelandservices.com</li>
      <li><svg viewBox="0 0 24 24"><circle cx="12" cy="12" r="10"/><path d="M2 12h20M12 2c3 3 3 17 0 20M12 2c-3 3-3 17 0 20" stroke="#fff" stroke-width="1.3" fill="none"/></svg>www.timberridgelandservices.com</li>
      <li><svg viewBox="0 0 24 24"><path d="M12 2a7 7 0 0 0-7 7c0 5 7 13 7 13s7-8 7-13a7 7 0 0 0-7-7zm0 9.5A2.5 2.5 0 1 1 12 6.5a2.5 2.5 0 0 1 0 5z"/></svg>00 dummy city, dummy place 0000</li>
    </ul>
  </div>
</section>

</body>
</html>
```